ad for food show brochure

Need to clean up this concept sketch. We are selling food at a festival but the concept isn't quite named. We're looking to create a buzz and have people sign up to be kept apprised of the progress of the chain ... or the first store. The website at the bottom is just for filler, we can add that before ad goes to print. We're not married to this text so if you come up with something better, great. also may want to have a blank @ line for twitter feed and another line for FB page.
The concept is for a Vegan Fast Food place but I need to focus more on the middle of the road diners, we'll get the vegans to come and staunch carnivores won't ever come so it's the middle of the road folks we're after. The slant and speed lines were my attempt to show speed.
Thanks.
This ad is a 5/5 x 2.125 space in the festival brochure. Need this asap.
I also think this needs to be b&w so lets go with that. Just found out COLOR is ok.
That last word in the sketch is not whose but WHERE?
The last word is WHERE not whose. Thanks
We either need to add the word Vegan in the top of the ad or add it in the sentence about all that is vegan and good in the worl.
The ad can be in color. Just to clarify, the word Vegan should be o e of the questions on top. Eithe as part of another question ... 'Vegan fast food?' Or as its own line or bubble.
- pdf file so I can change the website address.

```html
<!DOCTYPE html>
<html lang="en">
<head>
<meta charset="utf-8">
<title>Vegan Fast Food – Festival Ad</title>
<link href="https://fonts.googleapis.com/css2?family=Lilita+One&family=Fredoka:wght@600;700&display=swap" rel="stylesheet">
<style>
  :root {
    --page: #f2f2f2;
    --card: #ffffff;
    --green: #6cbe3c;
    --green-dark: #4c9a25;
    --magenta: #e6177e;
    --red: #e3261b;
    --sun-light: #ffe93a;
    --sun-mid: #ffc21c;
    --sun-deep: #f7901e;
    --bubble-line: #c9c9c9;
    --ink-shadow: rgba(0,0,0,0.25);
  }
  * { margin: 0; padding: 0; box-sizing: border-box; }
  html, body { width: 668px; height: 1200px; overflow: hidden; background: var(--page); }
  .ad {
    position: relative;
    width: 668px; height: 1200px;
    background: var(--card);
    border: 3px solid #e3e3e3;
    font-family: "Fredoka", sans-serif;
  }
  .headline { font-family: "Lilita One", sans-serif; line-height: 1; position: absolute; }
  .outlined {
    -webkit-text-stroke: 10px #fff;
    paint-order: stroke fill;
    filter: drop-shadow(2px 3px 2px var(--ink-shadow));
  }
  .brand-word {
    left: 62px; top: 30px;
    font-size: 92px; color: var(--green);
    letter-spacing: 1px;
  }
  .sun-panel {
    position: absolute;
    left: 14px; right: 14px; top: 139px; height: 784px;
    background: radial-gradient(circle at 30% 30%, var(--sun-light) 0%, var(--sun-mid) 45%, var(--sun-deep) 100%);
  }
  .bubble-tail { position: absolute; left: 250px; top: 136px; }
  .q-fastfood { left: 52px; top: 160px; font-size: 70px; color: var(--magenta); line-height: 0.93; }
  .q-mark { left: 345px; top: 150px; font-size: 178px; color: var(--magenta); }
  .q-soon { left: 52px; top: 412px; font-size: 58px; color: var(--green); line-height: 0.98; }
  .q-city { left: 52px; top: 604px; font-size: 64px; color: var(--magenta); }
  .food-icon { position: absolute; border-radius: 50%; border: 4px solid #fff; box-shadow: 1px 2px 3px var(--ink-shadow); }
  .icon-pizza  { left: 66px;  top: 318px; width: 64px; height: 64px; background: #f4a640; }
  .icon-burger { left: 162px; top: 318px; width: 70px; height: 64px; background: #3b8fd6; border-radius: 50% 50% 40% 40%; }
  .icon-hotdog { left: 52px;  top: 694px; width: 104px; height: 74px; background: #e8683a; border-radius: 40px; }
  .icon-donut  { left: 204px; top: 694px; width: 72px; height: 72px; background: #8ac640; }
  .answer {
    position: absolute;
    width: 116px; height: 58px;
    background: #fff;
    border: 2px solid var(--bubble-line);
    border-radius: 50%;
    font-family: "Lilita One", sans-serif;
    font-size: 30px; color: var(--magenta);
    display: flex; align-items: center; justify-content: center;
    box-shadow: 1px 2px 3px var(--ink-shadow);
  }
  .answer::after {
    content: ""; position: absolute; left: 16px; bottom: -12px;
    border-left: 8px solid transparent; border-right: 14px solid transparent;
    border-top: 16px solid #fff;
  }
  .answer-1 { left: 306px; top: 330px; }
  .answer-2 { left: 308px; top: 512px; }
  .answer-3 { left: 308px; top: 692px; }
  .plea {
    position: absolute; left: 0; right: 0; top: 800px;
    text-align: center; color: var(--red);
    font-weight: 700; font-size: 31px; line-height: 1.12;
  }
  .plea span { display: block; }
  .footer { position: absolute; left: 0; right: 0; top: 944px; text-align: center; font-weight: 700; color: var(--green-dark); }
  .site { font-size: 38px; }
  .tagline { margin-top: 18px; font-size: 44px; line-height: 1.1; }
  .tagline .product { color: var(--red); }
</style>
</head>
<body>
  <div class="ad">
    <div class="sun-panel"></div>
    <svg class="bubble-tail" width="80" height="50" viewBox="0 0 80 50" aria-hidden="true">
      <path d="M0 0 L60 0 L74 46 Z" fill="#fff"/>
    </svg>
    <div class="headline brand-word">VEGAN</div>

    <div class="headline outlined q-fastfood">FAST<br>FOOD</div>
    <div class="headline outlined q-mark">?</div>
    <div class="food-icon icon-pizza" role="img" aria-label="Pizza slice icon"></div>
    <div class="food-icon icon-burger" role="img" aria-label="Burger icon"></div>
    <div class="answer answer-1">YEP</div>

    <div class="headline outlined q-soon">COMMING<br>SOON?</div>
    <div class="answer answer-2">YEP</div>

    <div class="headline outlined q-city">IN NYC?</div>
    <div class="food-icon icon-hotdog" role="img" aria-label="Hot dog icon"></div>
    <div class="food-icon icon-donut" role="img" aria-label="Donut icon"></div>
    <div class="answer answer-3">YEP</div>

    <p class="plea">
      <span>In the Name of all that</span>
      <span>is good in the world....</span>
      <span>WHERE??</span>
    </p>

    <div class="footer">
      <p class="site">greenbite-eats.com</p>
      <p class="tagline">Today you can<br>enjoy our <span class="product">Crunchers</span></p>
    </div>
  </div>
</body>
</html>
```